Brochure/flyer for our trip to Paris

Our company is taking us all on a summer trip to Paris. We have some key information that we need to tell everybody about the trip. We think a nicely designed brochure or flyer, which uses our brand colours and guidelines, would be something nice to keep during the trip and as a memento afterwards.

We are looking for a brochure or a flyer which contains all the info in the attached document.

This needs to happen really fast as we actually go to Paris on the 13th August. We also need time to print it!

We can provide a library of icons. All images in the document can be changed. you don't have to use the images in the document.

Target Market(s)

People in our company. They are fun and as this is for a party the flyer needs to feel uplifting.

Industry/Entity Type

Health

Font styles to use
Other font styles liked:
• Nexa - please see attached font.

Requirements
Must have
• Designers must stick to our brand guideline, font and the colours we use.
• Please also see attached content for the flyer.
• This website shows our style - https://www.korilune.com/fr
Should not have
• Please don't make it too tacky or too much about French things. It can be a bit playful but not too much.

```html
<!DOCTYPE html>
<html lang="en">
<head>
<meta charset="utf-8">
<title>Korilune – Info Guide Paris 2016</title>
<link rel="stylesheet" href="https://fonts.googleapis.com/css2?family=Quicksand:wght@300;400;500;600;700&display=swap">
<style>
  :root {
    --canvas: #e8e8e8;
    --paper: #ffffff;
    --ink: #4a4a4a;
    --ink-dark: #222222;
    --teal: #7fcdc8;
    --teal-deep: #5ab8b2;
    --cyan: #1db4ec;
    --blue: #0b5aa9;
    --mist-top: rgba(255,255,255,0);
    --mist-photo: #c9ccd0;
    --cover-sky: #dfe3e6;
    --cover-ground: #b9bfc4;
  }
  * { box-sizing: border-box; margin: 0; padding: 0; }
  html, body { width: 1200px; height: 1000px; overflow: hidden; }
  body {
    background: var(--canvas);
    font-family: "Quicksand", sans-serif;
    color: var(--ink);
    position: relative;
  }

  /* Inside spread */
  .spread {
    position: absolute; left: 50px; top: 110px;
    width: 795px; height: 780px;
    display: flex;
    box-shadow: 0 10px 30px rgba(0,0,0,0.18);
    background: var(--paper);
  }
  .panel {
    position: relative; width: 265px; height: 100%;
    overflow: hidden;
    border-right: 1px solid #ececec;
  }
  .panel:last-child { border-right: none; }
  .panel__photo {
    position: absolute; left: 0; right: 0; bottom: 0; height: 62%;
    background: linear-gradient(to bottom, var(--mist-top) 0%, #e4e6e8 35%, var(--mist-photo) 100%);
  }
  .panel__header {
    position: relative; height: 58px;
    display: flex; align-items: center; justify-content: center; gap: 10px;
    color: #fff; font-size: 15px; font-weight: 500; letter-spacing: 0.5px;
  }
  .panel--helpful .panel__header { background: linear-gradient(90deg, var(--teal) 0%, #a5ddd9 100%); }
  .panel--legit .panel__header { background: var(--cyan); }
  .panel--smart .panel__header { background: var(--blue); }
  .panel__header svg { width: 22px; height: 22px; }
  .panel__body {
    position: relative; padding: 16px 18px 0;
    font-size: 11.5px; line-height: 1.5; text-align: justify;
  }
  .panel__body p { margin-bottom: 9px; }
  .section-title { font-weight: 700; font-size: 12.5px; margin-bottom: 6px; }
  .panel--helpful .section-title { color: var(--teal-deep); }
  .panel--legit .section-title { color: var(--cyan); }
  .panel--smart .section-title { color: var(--blue); }
  .day { font-weight: 700; color: var(--ink-dark); font-size: 12px; margin: 4px 0 4px; }
  .url { text-align: left; word-break: break-all; margin-top: 6px; }
  .contacts { list-style: none; margin-top: 4px; font-size: 13px; }
  .contacts li { display: flex; justify-content: space-between; padding: 3px 0; }
  .phrases { list-style: none; text-align: left; }
  .phrases li { margin-bottom: 3px; }

  .brand-block {
    position: absolute; left: 0; right: 0; bottom: 150px;
    display: flex; flex-direction: column; align-items: center; gap: 10px;
  }
  .brand-block__square { width: 64px; height: 64px; background: var(--cyan); }
  .brand-block__name { font-size: 20px; font-weight: 600; color: var(--blue); }

  /* Cover */
  .cover {
    position: absolute; left: 885px; top: 110px;
    width: 265px; height: 780px;
    background: var(--paper);
    box-shadow: 0 10px 30px rgba(0,0,0,0.18);
    overflow: hidden;
  }
  .cover__title {
    position: absolute; top: 80px; left: 0; right: 0; text-align: center;
  }
  .cover__name { font-size: 50px; font-weight: 400; color: var(--cyan); line-height: 1; }
  .cover__sub { font-size: 12px; color: var(--cyan); margin-top: 6px; letter-spacing: 0.3px; }
  .cover__photo {
    position: absolute; left: 0; right: 0; bottom: 0; height: 68%;
    background: linear-gradient(to bottom, #fbfbfc 0%, var(--cover-sky) 30%, #cfd4d8 70%, var(--cover-ground) 100%);
  }
</style>
</head>
<body>

<main class="spread" aria-label="Inside spread">
  <section class="panel panel--helpful">
    <div class="panel__photo" role="img" aria-label="Faded misty Paris rooftops photograph"></div>
    <header class="panel__header">
      <svg viewBox="0 0 24 24" fill="none" stroke="#fff" stroke-width="1.6" aria-hidden="true"><path d="M4 4h16v12H10l-4 4v-4H4z"/></svg>
      Helpful
    </header>
    <div class="panel__body">
      <h3 class="section-title">How to use the metro:</h3>
      <p>You have each been given 3 Metro tickets to help you on your way. Although you may need additional tickets depending on what your plans are in your free time.</p>
      <p>They are €4 for a single journey. Once you're in the Metro station, how to use the tickets is pretty self explanatory.</p>
      <p>Tip from Maëlle: the tickets have a magnetic strip so try and keep them away from bank cards etc. If you find that any of your tickets do not work, you can ask at the kiosk for a replacement.</p>
      <h3 class="section-title" style="margin-top:16px">Top Tips:</h3>
      <p>The best way to find your way around is to use RouteFinder or alternatively:</p>
      <p class="url">http://www.metrolis-paris.fr/itineraires/en/trajet/avance</p>
      <h3 class="section-title" style="margin-top:18px">Emergency Internal Contacts:</h3>
      <ul class="contacts">
        <li><span>Maren</span><span>07700 900118</span></li>
        <li><span>Tobias</span><span>07700 900246</span></li>
        <li><span>Oliver</span><span>07700 900375</span></li>
        <li><span>Lina</span><span>07700 900482</span></li>
      </ul>
    </div>
  </section>

  <section class="panel panel--legit">
    <div class="panel__photo" role="img" aria-label="Faded misty photograph of Paris with the Eiffel Tower"></div>
    <header class="panel__header">
      <svg viewBox="0 0 24 24" fill="none" stroke="#fff" stroke-width="1.6" aria-hidden="true"><rect x="4" y="6" width="14" height="14"/><path d="M20 2v6M17 5h6"/></svg>
      Legitimate
    </header>
    <div class="panel__body">
      <h3 class="section-title">Itinerary</h3>
      <p class="day">13th August</p>
      <p>Arrive in Paris at 11:17am local time. Drop bags to hotel, grab lunch and enjoy our 1 hour River Seine Tour.</p>
      <p class="day">Free time2:</p>
      <p>3:07pm (you will need to go and officially check in at the hotel and get ready for the evening within this time)</p>
      <p>7pm: Drinks and dinner at……<br>Late night drinks at……</p>
      <p class="day">The next day…..</p>
      <p>Check out between 9:10am at the latest and enjoy some breakfast at the hotel.</p>
      <p>Casual walk up to Gare du Nord, enjoying Paris that little bit more before we leave.</p>
      <p>Everyone must be at Gare du Nord by 2pm at the very latest to check in!</p>
    </div>
    <div class="brand-block">
      <div class="brand-block__square" aria-hidden="true"></div>
      <span class="brand-block__name">Korilune</span>
    </div>
  </section>

  <section class="panel panel--smart">
    <div class="panel__photo" role="img" aria-label="Faded misty Paris street photograph"></div>
    <header class="panel__header">
      <svg viewBox="0 0 24 24" fill="none" stroke="#fff" stroke-width="1.6" aria-hidden="true"><path d="M12 3v3M5 6l2 2M19 6l-2 2"/><circle cx="12" cy="15" r="5"/></svg>
      Smart
    </header>
    <div class="panel__body">
      <h3 class="section-title">Some Mustknow</h3>
      <p style="text-align:left">French Phrases for Savvy Travellers:</p>
      <ol class="phrases">
        <li>1. Bonjour. (Hello)</li>
        <li>2. Oui / Non (Yes / No)</li>
        <li>3. Parlezvous anglais ? (Do you speak English?)</li>
        <li>4. Où est le métro? (Where is the Metro?)</li>
        <li>5. Où est…? (Where is…?)</li>
        <li>6. Où est le guichet ? (Where is the ticket window?)</li>
        <li>7. Combien ça coûte? (How much does it cost?)</li>
        <li>8. Merci (Thank you)</li>
        <li>9. Bonsoir (Hello/good evening)</li>
        <li>10. Au Revoir (Goodbye)</li>
        <li>11. Puisje me connecter à internet ? (Can I get on the internet?)</li>
        <li>12. Je ne comprends pas (I don't understand)</li>
        <li>13. Je ne sais pas (I don't know)</li>
        <li>14. Estce que vous pouvez m'aider ? (Could you please help me?)</li>
        <li>15. Pouvezvous répéter, s'il vous plaît? (Could you repeat that?)</li>
      </ol>
    </div>
  </section>
</main>

<section class="cover" aria-label="Front cover">
  <div class="cover__photo" role="img" aria-label="Photograph of a girl in a pink dress holding red balloons in front of the Eiffel Tower on a misty day"></div>
  <div class="cover__title">
    <h1 class="cover__name">Korilune</h1>
    <p class="cover__sub">Info Guide Paris 2016</p>
  </div>
</section>

</body>
</html>
```